Professional Website Design to match new logo for Medical Legal Company

We have rebranded our company and We want a professional but also dynamic web site design for a group of esteemed doctors that provide expert evaluation of an injured worker in a Workers Compensation case.
​
1. Our target market is both the attorneys who select our doctors and any doctors who would wish to join our group.

2. Notes for the Landing Page:
- We prefer a simpler, sleeker more modern look for the landing page.
- We want a simplified landing page with one image, three buttons highlighted in Content document.
- We want the main image to be black and white but it can be splashed with color.
-We think the landing page might be enhanced by add a dark blue or black as a primary color. Of course please feel free to try any color combination you think might work.
- We want "The Meridale Circle" in large letters and "Stewards of a fair and prompt outcome" in small lettering. We don't want icons on the buttons.
- Do not want more than the one picture at top of landing page.
- We do not want any pictures that include faces. Please eliminate or replace. They will not be chosen.
- For the landing page, instead of a second set of photos please experiment with using medical symbols and legal symbols.
​
3. New Company Name: The Meridale Circle
New logo is uploaded bronze and grey/silver will be colors although we are still tweaking the colors for more metallic feel. Want simple not busy.

4. The overall Web page design needs to have some website design effect (e,g image rollover, scrolling effect, hover effect etc).

5. Please follow the attached word document file for the page content of the 4 web pages. Do not mix it up.

Previous company website: www.clinicjuristpanel.example (we wish to convert some of the content from this website to the new brand). Competitor website that we like: www.docboardly.example

Target Market(s)

Professional Elite. Attorneys and Doctors

Industry/Entity Type

Medical Legal

Coding

Coded - Design and coding required

Number of Pages Required

5+ page

Font styles to use
Other font styles liked:
• Helvetica or maybe font that matches logo. We are open

Colors

Designer to choose colors to be used in the design.

Requirements
Must have
• I can't locate on color scale but we want Bronze and Silver/Grey from logo. Additional colors can be added. Various shades of grey
Nice to have
• Black and white photos, simple elegant design
Should not have
• Images with faces of unknown people

```html
<!DOCTYPE html>
<html lang="en">
<head>
<meta charset="utf-8">
<title>The Meridale Circle — Medical Reporting</title>
<link href="https://fonts.googleapis.com/css2?family=Libre+Caslon+Text&family=Open+Sans:wght@400;600;700&display=swap" rel="stylesheet">
<style>
:root{
  --navy:#1b3468;
  --navy-text:#1f3a6e;
  --footer:#0c3a5e;
  --bronze:#c98354;
  --bronze-deep:#a8643a;
  --grey:#5a5f66;
  --ink:#1d1d1d;
  --rule:#e6e6e6;
  --white:#ffffff;
}
*{margin:0;padding:0;box-sizing:border-box}
html,body{width:825px;height:1200px;overflow:hidden;background:var(--white)}
body{position:relative;font-family:"Open Sans",Arial,sans-serif;color:var(--ink)}
.brand{position:absolute;left:44px;top:14px;display:flex;align-items:center;gap:8px}
.brand-mark{width:22px;height:22px;background:var(--grey)}
.brand-name{font-family:"Libre Caslon Text",Georgia,serif;font-size:16px;color:var(--grey);letter-spacing:.5px}
.hero-photo{position:absolute;left:0;top:0}
.commitment{position:absolute;left:46px;top:134px;width:520px}
.commitment h1{font-family:"Libre Caslon Text",Georgia,serif;font-weight:400;font-size:16.6px;line-height:23.5px;letter-spacing:0;color:var(--ink);text-transform:uppercase;white-space:nowrap;width:336px}
.commitment .intro{margin-top:5px;font-size:9.6px;line-height:14.2px}
.standards{list-style:none;margin-top:6px;font-size:8.8px;line-height:15px}
.standards li{padding-left:8px;text-indent:-8px}
.standards li::before{content:"- ";padding-right:2px}
.standards b{font-weight:700}
.divider{position:absolute;left:73px;top:437px;width:679px;height:1px;background:var(--rule)}
.action-card{position:absolute;width:169px;height:94px;background:var(--navy);color:var(--white)}
.action-card svg.icon{position:absolute;left:11px;top:11px}
.action-card .rule{position:absolute;left:10px;right:10px;top:50px;height:1px;background:rgba(255,255,255,.18)}
.action-card .title{position:absolute;left:11px;top:59px;width:150px;font-family:"Libre Caslon Text",Georgia,serif;font-size:10px;line-height:12px}
.action-card .arrow{position:absolute;right:9px;bottom:6px}
.services-photo{position:absolute;left:0;top:720px;width:497px;height:347px;border-top-right-radius:10px;background:linear-gradient(120deg,#1e3f77 0%,#2f5b9a 45%,#6f9ccf 80%,#a9c6e6 100%)}
.services{position:absolute;left:525px;top:745px;list-style:none}
.services li{display:flex;align-items:center;gap:6px;height:25px;font-size:12.4px;color:var(--navy-text)}
.site-footer{position:absolute;left:0;top:1067px;width:825px;height:133px;background:var(--footer);color:var(--white)}
.footer-links{position:absolute;top:33px;width:100%;text-align:center;font-size:7.4px}
.footer-links span{margin:0 4px}
.footer-rule{position:absolute;left:146px;top:58px;width:532px;height:1px;background:rgba(255,255,255,.2)}
.hq{position:absolute;left:165px;top:76px;font-size:9.4px;line-height:14px}
.hq strong,.contact strong{font-weight:700}
.contact{position:absolute;left:432px;top:76px;font-size:9.2px;line-height:13px}
.social{position:absolute;left:590px;top:75px;display:flex;gap:4px}
.social i{display:block;width:20px;height:20px;border-radius:50%;background:var(--white)}
</style>
</head>
<body>

<svg class="hero-photo" width="825" height="410" viewBox="0 0 825 410" role="img" aria-label="Photo of two businesspeople shaking hands over printed charts, in warm bronze tones">
  <defs>
    <linearGradient id="heroTone" x1="0" y1="0" x2="1" y2="1">
      <stop offset="0" stop-color="#e9c9a8"/>
      <stop offset=".5" stop-color="#d9a57c"/>
      <stop offset="1" stop-color="#b67a55"/>
    </linearGradient>
  </defs>
  <path d="M463 0 L378 92 Q366 110 381 127 L640 394 Q657 410 674 394 L825 244 L825 0 Z" fill="url(#heroTone)"/>
  <path d="M378 92 Q366 110 381 127 L640 394 Q657 410 674 394 L825 244" fill="none" stroke="var(--bronze)" stroke-width="5"/>
</svg>

<div class="brand">
  <i class="brand-mark"></i>
  <span class="brand-name">THE MERIDALE CIRCLE</span>
</div>

<section class="commitment">
  <h1>Commitment to the Highest<br>Standard of Medical Reporting</h1>
  <p class="intro">The Meridale Circle strives to uphold the Highest Standard in Medical Reporting.<br>Following is a list to best describe what to expect when you receive QME<br>Report from one of our Stewards:</p>
  <ul class="standards">
    <li><b>Timely:</b> Unless special circumstances exist, you can expect to receive the report<br>well ahead of DWC imposed deadlines</li>
    <li>Clear, Concise and Readable:&nbsp; So your valuable time is not wasted</li>
    <li><b>Impartial:</b> (all of our reports are reviewed by a 3rd party for Objectivity</li>
    <li>High Level Review of Records by the Physician with Commentary</li>
    <li>Detailed and Comprehensive Medical History</li>
    <li>No Conclusory Findings:&nbsp; Thoroughly discussed conclusions for Apportionment,<br>Causation and Impairment that are medical evidence based</li>
    <li>Comprehensive Analysis of all injured body parts focused on the medical, not legal aspects of the case</li>
    <li>Answers to all questions stated in the Cover Letter</li>
    <li style="white-space:nowrap">Future Medical Care Section that is thoughtful and addresses both the short term and long term needs of the applicant</li>
  </ul>
</section>

<div class="divider"></div>

<a class="action-card" style="left:56px;top:477px">
  <svg class="icon" width="30" height="32" viewBox="0 0 30 32" fill="none" stroke="#fff" stroke-width="1.2"><rect x="7" y="3" width="16" height="22" rx="1"/><path d="M11 9h8M11 13h8M11 17h6"/><circle cx="7" cy="25" r="5"/><path d="M7 22v3h2"/><path d="M22 12l6-9"/></svg>
  <i class="rule"></i><span class="title">Schedule An Exam</span>
  <svg class="arrow" width="8" height="8" viewBox="0 0 8 8" fill="none" stroke="#fff" stroke-width="1"><path d="M1 4h6M4.5 1.5L7 4 4.5 6.5"/></svg>
</a>
<a class="action-card" style="left:237px;top:477px">
  <svg class="icon" width="30" height="32" viewBox="0 0 30 32" fill="none" stroke="#fff" stroke-width="1.2"><path d="M3 2h17l5 5v23H3z"/><rect x="7" y="9" width="3" height="3"/><rect x="7" y="15" width="3" height="3"/><rect x="7" y="21" width="3" height="3"/><path d="M13 10h8M13 16h8M13 22h8"/></svg>
  <i class="rule"></i><span class="title">Contact Us with Questions regarding Upcoming Exam</span>
  <svg class="arrow" width="8" height="8" viewBox="0 0 8 8" fill="none" stroke="#fff" stroke-width="1"><path d="M1 4h6M4.5 1.5L7 4 4.5 6.5"/></svg>
</a>
<a class="action-card" style="left:417px;top:477px">
  <svg class="icon" width="32" height="32" viewBox="0 0 32 32" fill="none" stroke="#fff" stroke-width="1.2"><rect x="2" y="3" width="26" height="26" rx="1"/><rect x="6" y="8" width="5" height="5"/><rect x="6" y="16" width="5" height="5"/><path d="M14 9h10M14 12h10M14 17h10M14 20h6"/><path d="M23 30v-7l3 1v6"/></svg>
  <i class="rule"></i><span class="title">Medical Records Upload</span>
  <svg class="arrow" width="8" height="8" viewBox="0 0 8 8" fill="none" stroke="#fff" stroke-width="1"><path d="M1 4h6M4.5 1.5L7 4 4.5 6.5"/></svg>
</a>
<a class="action-card" style="left:598px;top:477px">
  <svg class="icon" width="32" height="32" viewBox="0 0 32 32" fill="none" stroke="#fff" stroke-width="1.2"><circle cx="12" cy="14" r="5"/><path d="M4 30c0-6 4-9 8-9s8 3 8 9"/><circle cx="25" cy="6" r="4"/><path d="M24 5a1 1 0 1 1 1 2v1"/><path d="M19 16v1"/></svg>
  <i class="rule"></i><span class="title">Information Request</span>
  <svg class="arrow" width="8" height="8" viewBox="0 0 8 8" fill="none" stroke="#fff" stroke-width="1"><path d="M1 4h6M4.5 1.5L7 4 4.5 6.5"/></svg>
</a>
<a class="action-card" style="left:328px;top:582px">
  <svg class="icon" width="36" height="32" viewBox="0 0 36 32" fill="none" stroke="#fff" stroke-width="1.2"><ellipse cx="18" cy="10" rx="15" ry="6"/><circle cx="14" cy="10" r="3"/><circle cx="20" cy="15" r="3"/><circle cx="12" cy="21" r="3"/><circle cx="22" cy="25" r="3"/><path d="M18 2v4M16 4h4M6 27h4M8 25v4"/></svg>
  <i class="rule"></i><span class="title">Supplemental Request</span>
  <svg class="arrow" width="8" height="8" viewBox="0 0 8 8" fill="none" stroke="#fff" stroke-width="1"><path d="M1 4h6M4.5 1.5L7 4 4.5 6.5"/></svg>
</a>

<div class="services-photo" role="img" aria-label="Photo of hands typing on a laptop with floating blue quality and certification icons"></div>

<ul class="services">
  <li><svg width="11" height="11" viewBox="0 0 12 12" fill="none" stroke="currentColor" stroke-width="1.2"><path d="M10.5 6A4.5 4.5 0 1 1 8 2"/><path d="M4 6l2 2 5-5"/></svg>IME</li>
  <li><svg width="11" height="11" viewBox="0 0 12 12" fill="none" stroke="currentColor" stroke-width="1.2"><path d="M10.5 6A4.5 4.5 0 1 1 8 2"/><path d="M4 6l2 2 5-5"/></svg>AME</li>
  <li><svg width="11" height="11" viewBox="0 0 12 12" fill="none" stroke="currentColor" stroke-width="1.2"><path d="M10.5 6A4.5 4.5 0 1 1 8 2"/><path d="M4 6l2 2 5-5"/></svg>QME</li>
  <li><svg width="11" height="11" viewBox="0 0 12 12" fill="none" stroke="currentColor" stroke-width="1.2"><path d="M10.5 6A4.5 4.5 0 1 1 8 2"/><path d="M4 6l2 2 5-5"/></svg>Subsequent Injuries Fund</li>
  <li><svg width="11" height="11" viewBox="0 0 12 12" fill="none" stroke="currentColor" stroke-width="1.2"><path d="M10.5 6A4.5 4.5 0 1 1 8 2"/><path d="M4 6l2 2 5-5"/></svg>Ergonomic Evaluations</li>
  <li><svg width="11" height="11" viewBox="0 0 12 12" fill="none" stroke="currentColor" stroke-width="1.2"><path d="M10.5 6A4.5 4.5 0 1 1 8 2"/><path d="M4 6l2 2 5-5"/></svg>Measuring Workers</li>
  <li><svg width="11" height="11" viewBox="0 0 12 12" fill="none" stroke="currentColor" stroke-width="1.2"><path d="M10.5 6A4.5 4.5 0 1 1 8 2"/><path d="M4 6l2 2 5-5"/></svg>Pre-Employment Screenings</li>
  <li><svg width="11" height="11" viewBox="0 0 12 12" fill="none" stroke="currentColor" stroke-width="1.2"><path d="M10.5 6A4.5 4.5 0 1 1 8 2"/><path d="M4 6l2 2 5-5"/></svg>Fit for Duty</li>
  <li><svg width="11" height="11" viewBox="0 0 12 12" fill="none" stroke="currentColor" stroke-width="1.2"><path d="M10.5 6A4.5 4.5 0 1 1 8 2"/><path d="M4 6l2 2 5-5"/></svg>Functional Capacity Evaluation</li>
  <li><svg width="11" height="11" viewBox="0 0 12 12" fill="none" stroke="currentColor" stroke-width="1.2"><path d="M10.5 6A4.5 4.5 0 1 1 8 2"/><path d="M4 6l2 2 5-5"/></svg>Physician’s Guide</li>
  <li><svg width="11" height="11" viewBox="0 0 12 12" fill="none" stroke="currentColor" stroke-width="1.2"><path d="M10.5 6A4.5 4.5 0 1 1 8 2"/><path d="M4 6l2 2 5-5"/></svg>Impairment Rating</li>
  <li><svg width="11" height="11" viewBox="0 0 12 12" fill="none" stroke="currentColor" stroke-width="1.2"><path d="M10.5 6A4.5 4.5 0 1 1 8 2"/><path d="M4 6l2 2 5-5"/></svg>Continuing Education</li>
</ul>

<footer class="site-footer">
  <nav class="footer-links">Continuing Education Courses<span>|</span>QME Test Resources<span>|</span>Newsletter<span>|</span>Upcoming Events<span>|</span>Current Member Login<span>|</span>Contact Us<span>|</span>Sitemap</nav>
  <i class="footer-rule"></i>
  <div class="hq"><strong>HEADQUARTERS</strong><br>2280 Larkspur Ave., 3rd Floor, Fairhaven, CA 90411</div>
  <div class="contact"><strong>Call toll free</strong> (800) 555-0142<br><strong>Fax</strong> (310) 555-0178</div>
  <div class="social"><i></i><i></i><i></i></div>
</footer>

</body>
</html>
```